Assisted living facility needs a business card design

We need a business card design for an assisted living facility in Los Angeles. We have a logo selected but we would like a business card design that will leave a lasting impression on families looking to place their elderly loved ones in our care as well as on other facility providers who may refer their elderly residents to our facility.

```html
<!DOCTYPE html>
<html lang="en">
<head>
<meta charset="utf-8">
<title>Maplecrest Haven Senior Living – Business Card</title>
<link href="https://fonts.googleapis.com/css2?family=Cinzel:wght@400&family=Arimo:wght@400&display=swap" rel="stylesheet">
<style>
  :root {
    --backdrop: #3d3d3d;
    --card-white: #ffffff;
    --brand-blue: #0b66c0;
    --band-grey: #5e5e5e;
    --text-grey: #4a4a4a;
    --rule-grey: #cfcfcf;
    --serif: "Cinzel", "Times New Roman", serif;
    --sans: "Arimo", Arial, sans-serif;
  }
  * { box-sizing: border-box; margin: 0; padding: 0; }
  html, body { width: 1200px; height: 803px; overflow: hidden; background: var(--backdrop); }
  .canvas { position: relative; width: 1200px; height: 803px; }

  .card {
    position: absolute;
    top: 247px;
    width: 540px;
    height: 309px;
    border-radius: 22px;
    overflow: hidden;
    box-shadow: 0 14px 30px rgba(0,0,0,.45);
  }
  .card--front { left: 40px; background: var(--card-white); }
  .card--back  { left: 620px; background: var(--brand-blue); }

  /* front */
  .front-bands { position: absolute; inset: 0; }
  .wordmark {
    position: absolute;
    font-family: var(--serif);
    font-weight: 400;
    color: var(--brand-blue);
    text-align: center;
    line-height: 1.05;
    letter-spacing: 1px;
  }
  .card--front .wordmark { right: 34px; top: 42px; width: 290px; font-size: 27px; }
  .wordmark .wordmark-sub { display: block; font-size: 11px; letter-spacing: 6px; margin-top: 8px; }

  .person { position: absolute; left: 36px; top: 168px; }
  .person-name { font-family: var(--serif); color: var(--brand-blue); font-size: 24px; letter-spacing: 1px; }
  .person-role { font-family: var(--sans); color: var(--text-grey); font-size: 12px; margin-top: 1px; }

  .divider { position: absolute; left: 36px; right: 36px; top: 214px; height: 1px; background: var(--rule-grey); }

  .contacts { position: absolute; left: 36px; top: 222px; list-style: none; font-family: var(--sans); font-size: 12.5px; color: var(--text-grey); }
  .contacts li { display: flex; align-items: center; gap: 8px; height: 17px; }
  .contacts svg { width: 11px; height: 11px; fill: var(--brand-blue); }

  .address { position: absolute; right: 36px; top: 168px; text-align: right; font-family: var(--sans); font-size: 13px; color: var(--text-grey); line-height: 1.4; }
  .website { position: absolute; right: 36px; bottom: 10px; font-family: var(--sans); font-size: 13px; color: var(--card-white); }

  /* back */
  .card--back .wordmark { left: 0; right: 0; top: 108px; margin: auto; width: 440px; color: var(--card-white); font-size: 40px; }
  .card--back .wordmark .wordmark-sub { font-size: 14px; letter-spacing: 9px; margin-top: 12px; }
</style>
</head>
<body>
<main class="canvas">

  <section class="card card--front" aria-label="Business card front">
    <svg class="front-bands" viewBox="0 0 540 309" preserveAspectRatio="none" aria-hidden="true">
      <polygon points="0,299 300,299 312,280 540,280 540,309 0,309" fill="var(--brand-blue)"/>
      <polygon points="0,294 296,294 306,277 312,280 300,299 0,299" fill="var(--band-grey)"/>
    </svg>

    <div class="wordmark">MAPLECREST HAVEN<span class="wordmark-sub">SENIOR LIVING</span></div>

    <div class="person">
      <p class="person-name">DANIEL HARTLEY</p>
      <p class="person-role">President</p>
    </div>

    <div class="address">
      <p>1426 Willow Bend Road</p>
      <p>Glenfield, Canada 20418</p>
    </div>

    <div class="divider"></div>

    <ul class="contacts">
      <li>
        <svg viewBox="0 0 24 24" aria-hidden="true"><path d="M6.6 10.8a15 15 0 0 0 6.6 6.6l2.2-2.2a1 1 0 0 1 1-.25 11.4 11.4 0 0 0 3.6.57 1 1 0 0 1 1 1V20a1 1 0 0 1-1 1A17 17 0 0 1 3 4a1 1 0 0 1 1-1h3.5a1 1 0 0 1 1 1c0 1.25.2 2.45.57 3.6a1 1 0 0 1-.25 1z"/></svg>
        <span>555-210-4837</span>
      </li>
      <li>
        <svg viewBox="0 0 24 24" aria-hidden="true"><path d="M7 1h10a2 2 0 0 1 2 2v18a2 2 0 0 1-2 2H7a2 2 0 0 1-2-2V3a2 2 0 0 1 2-2zm0 3v14h10V4z"/></svg>
        <span>555-318-2094</span>
      </li>
      <li>
        <svg viewBox="0 0 24 24" aria-hidden="true"><path d="M2 5h20v14H2zm2 2v.5l8 5 8-5V7z"/></svg>
        <span>info@maplecresthaven.com</span>
      </li>
    </ul>

    <p class="website">www.maplecresthaven.com</p>
  </section>

  <section class="card card--back" aria-label="Business card back">
    <div class="wordmark">MAPLECREST HAVEN<span class="wordmark-sub">SENIOR LIVING</span></div>
  </section>

</main>
</body>
</html>
```